Business cards and stationary for zombie fantasy camp
The Bramble Lodge
Business cards and stationary for zombie fantasy camp - Outdoors
Creative Brief
Simple
Jordan Reyes
14 Fernway Rd Millbrook
hello@thebramblelodge.example
www.thebramblelodge.example
Please refer to the website to get ideas as to what to add to this business card. I would like a design that speaks to the nature of the business. I have also uploaded 4 different logo's that I use, please feel free to experiment with each one. I'm in need of business cards, stationary, presentation folders, etc...
Please refer to the website to get ideas as to what to add to this business card. I would like a design that speaks to the nature of the business.
Tovick88 Tovick88
Attention please all designers: I've extended this contest for 3 days, not so much to find new designs but many of you have submitted designs that are nearing what I'm looking for. And the three days will enable us all time to communicate and work through those changes. I don't want any of you missing out because I didn't get online until only the final hours risking being able to give you all a chance to make those modifications I'm looking for. Sorry for the delay, But, thank you for your patience and all of your work.
All designers please note, you each that have submitted ideas have some excellent business card ideas, There is only 1 day left, please stop concentrating on business cards, and start focusing on stationary, letterheads, envelopes, and email signatures, I'm looking for the whole package here.
Just a quick message to thank everyone for the work that they have put into my project, I've got some excellent designs. With that being said, I still would like to see more designs for items specifically with Presentation Folders, Stationary, envelopes, and email signatures
Feel free to use any logo that I have uploaded here. I like all of them, so I look forward to seeing what you can do with any one of them or all of them.
My project had started once before, quillhaven had noticed that I had a logo project running at the same time, so they made the recommendation to put this on hold until that project finished. To the designers that submitted already, I apologize to you all. The logo project is now finished, I had multiple logo's I likes so I've posted them here for you to use as your inspiration. Good luck to you all and with all projects, I look forward to seeing your work.
I will be looking to use these designs when ordering business cards through prenta nook.example, I'm also looking for designs for stationary, envelopes and presentation folders all ordered through prentanook.example

```html
<!DOCTYPE html>
<html lang="en">
<head>
<meta charset="utf-8">
<title>The Bramble Lodge – Stationery Set</title>
<link href="https://fonts.googleapis.com/css2?family=Oswald:wght@700&family=Roboto:wght@400;500&display=swap" rel="stylesheet">
<style>
  :root{
    --stage:#1d7a3c;
    --paper:#ffffff;
    --ink:#141414;
    --gold:#e8a317;
    --gold-light:#f6c641;
    --label:#e8f3ea;
  }
  *{box-sizing:border-box;margin:0;padding:0}
  html,body{width:1200px;height:269px;overflow:hidden}
  body{background:var(--stage);position:relative;font-family:"Roboto",Arial,sans-serif}
  .piece{position:absolute;background:var(--paper);overflow:hidden;box-shadow:0 1px 3px rgba(0,0,0,.35)}
  .piece svg.swoosh{position:absolute;left:0;top:0;width:100%;height:100%}
  .label{position:absolute;font-size:7px;color:var(--label);font-weight:500;white-space:nowrap}
  .brand{position:absolute;display:flex;align-items:center;gap:3px;white-space:nowrap}
  .brand-mark{width:10px;height:10px;border-radius:50%;background:var(--gold);flex:none}
  .brand-name{font-family:"Oswald",Impact,sans-serif;font-weight:700;color:var(--ink);text-transform:uppercase;line-height:1}
  .figure{position:absolute;background:linear-gradient(#444,#111);border-radius:3px}
  .figure.faint{background:linear-gradient(#e2e2e2,#cfcfcf)}
  .contact{position:absolute;font-size:5px;line-height:7px;color:var(--ink);white-space:nowrap}
  .contact strong{font-weight:500}
</style>
</head>
<body>

<!-- Front card -->
<span class="label" style="left:150px;top:6px">Paper Letter</span>
<div class="piece front-card" style="left:8px;top:24px;width:184px;height:80px">
  <svg class="swoosh" viewBox="0 0 184 80" preserveAspectRatio="none">
    <path d="M0 60 Q60 40 120 58 T184 50 V80 H0Z" fill="var(--gold)"/>
    <path d="M0 66 Q60 50 120 66 T184 60 V80 H0Z" fill="var(--ink)"/>
  </svg>
  <div class="figure" style="left:22px;top:8px;width:26px;height:32px" role="img" aria-label="Silhouette emblem"></div>
  <div class="brand" style="left:14px;top:42px"><span class="brand-mark"></span><span class="brand-name" style="font-size:8px">The Bramble Lodge</span></div>
</div>
<span class="label" style="left:90px;top:107px">Front Card</span>

<!-- Back card -->
<div class="piece back-card" style="left:8px;top:132px;width:184px;height:88px">
  <svg class="swoosh" viewBox="0 0 184 88" preserveAspectRatio="none">
    <path d="M0 72 Q70 60 130 74 T184 68 V88 H0Z" fill="var(--gold)"/>
    <path d="M0 78 Q70 68 130 80 T184 76 V88 H0Z" fill="var(--ink)"/>
  </svg>
  <div class="figure" style="left:24px;top:8px;width:28px;height:34px" role="img" aria-label="Silhouette emblem"></div>
  <div class="brand" style="left:14px;top:46px"><span class="brand-mark"></span><span class="brand-name" style="font-size:8px">The Bramble Lodge</span></div>
  <div class="contact" style="left:104px;top:16px">
    <strong>Jordan Reyes</strong><br>14 Fernway Rd Millbrook<br>hello@thebramblelodge.example<br>www.thebramblelodge.example
  </div>
</div>
<span class="label" style="left:90px;top:224px">Back Card</span>

<!-- Folder -->
<div class="piece folder" style="left:209px;top:17px;width:391px;height:218px">
  <svg class="swoosh" viewBox="0 0 391 218" preserveAspectRatio="none">
    <defs>
      <linearGradient id="folderDark" x1="0" y1="0" x2="1" y2="1">
        <stop offset="0" stop-color="#2a2a2a"/><stop offset=".6" stop-color="#0d0d0d"/><stop offset="1" stop-color="#6b4a0c"/>
      </linearGradient>
      <linearGradient id="folderGold" x1="0" y1="0" x2="1" y2="0">
        <stop offset="0" stop-color="#e8a317"/><stop offset="1" stop-color="#7a5410"/>
      </linearGradient>
    </defs>
    <rect width="391" height="218" fill="url(#folderDark)"/>
    <path d="M0 0 H391 V90 Q300 140 200 110 T0 130Z" fill="var(--paper)"/>
    <path d="M0 130 Q100 100 200 118 T391 96 V108 Q300 150 200 128 T0 146Z" fill="url(#folderGold)"/>
  </svg>
  <div class="figure" style="left:36px;top:14px;width:52px;height:62px" role="img" aria-label="Silhouette emblem"></div>
  <div class="brand" style="left:26px;top:80px"><span class="brand-mark" style="width:14px;height:14px"></span><span class="brand-name" style="font-size:13px">The Bramble Lodge</span></div>
  <div class="figure" style="left:230px;top:14px;width:60px;height:70px;background:linear-gradient(#7a7a7a,#3a3a3a)" role="img" aria-label="Soldier silhouette with scattered zombie hands"></div>
</div>
<span class="label" style="left:395px;top:237px">Poster</span>

<!-- Letterhead -->
<div class="piece letterhead" style="left:619px;top:19px;width:185px;height:228px">
  <svg class="swoosh" viewBox="0 0 185 228" preserveAspectRatio="none">
    <path d="M0 200 Q70 180 120 198 T185 190 V228 H0Z" fill="var(--gold)"/>
    <path d="M0 210 Q70 194 120 210 T185 204 V228 H0Z" fill="var(--ink)"/>
  </svg>
  <div class="brand" style="left:10px;top:8px"><span class="brand-mark" style="width:8px;height:8px"></span><span class="brand-name" style="font-size:6px">The Bramble Lodge</span></div>
  <div class="figure faint" style="left:62px;top:56px;width:60px;height:80px" role="img" aria-label="Faint silhouette watermark"></div>
</div>
<span class="label" style="left:690px;top:250px">Letter Head</span>

<!-- Report letter card -->
<span class="label" style="left:905px;top:14px">Report Letter</span>
<div class="piece mini-card" style="left:818px;top:24px;width:140px;height:78px">
  <svg class="swoosh" viewBox="0 0 140 78" preserveAspectRatio="none">
    <path d="M0 58 Q50 44 90 58 T140 52 V78 H0Z" fill="var(--gold)"/>
    <path d="M0 64 Q50 52 90 64 T140 60 V78 H0Z" fill="var(--ink)"/>
  </svg>
  <div class="figure" style="left:12px;top:8px;width:20px;height:26px" role="img" aria-label="Silhouette emblem"></div>
  <div class="brand" style="left:8px;top:38px"><span class="brand-mark" style="width:7px;height:7px"></span><span class="brand-name" style="font-size:6px">The Bramble Lodge</span></div>
</div>

<!-- Front card, right -->
<div class="piece mini-card" style="left:968px;top:92px;width:140px;height:62px">
  <svg class="swoosh" viewBox="0 0 140 62" preserveAspectRatio="none">
    <path d="M0 44 Q50 34 90 46 T140 40 V62 H0Z" fill="var(--gold)"/>
    <path d="M0 50 Q50 42 90 52 T140 48 V62 H0Z" fill="var(--ink)"/>
  </svg>
</div>
<span class="label" style="left:1000px;top:157px">Front Card</span>

<!-- Business card -->
<div class="piece mini-card" style="left:818px;top:135px;width:140px;height:80px">
  <svg class="swoosh" viewBox="0 0 140 80" preserveAspectRatio="none">
    <path d="M0 60 Q50 46 90 60 T140 54 V80 H0Z" fill="var(--gold)"/>
    <path d="M0 66 Q50 54 90 66 T140 62 V80 H0Z" fill="var(--ink)"/>
  </svg>
  <div class="figure" style="left:12px;top:8px;width:20px;height:26px" role="img" aria-label="Silhouette emblem"></div>
  <div class="brand" style="left:8px;top:38px"><span class="brand-mark" style="width:7px;height:7px"></span><span class="brand-name" style="font-size:6px">The Bramble Lodge</span></div>
</div>
<span class="label" style="left:900px;top:220px">Business Card</span>

<!-- Envelope back -->
<svg class="envelope-back" style="position:absolute;left:972px;top:166px" width="216" height="70" viewBox="0 0 216 70">
  <rect x="0" y="0" width="216" height="70" fill="var(--paper)"/>
  <rect x="0" y="0" width="216" height="14" fill="var(--gold)"/>
  <rect x="0" y="14" width="216" height="8" fill="var(--ink)"/>
  <rect x="0" y="40" width="216" height="8" fill="var(--gold-light)"/>
  <rect x="0" y="48" width="216" height="6" fill="var(--ink)"/>
</svg>
<span class="label" style="left:1140px;top:252px">Envelope Back</span>

</body>
</html>
```